App Design for quiz app (casual gaming app)

We need an design & logo for our quiz app. Its a simple quiz app, where you pick up a category, answer three questions out of this category. After this an opponent is assigned to your game, and has to answer the same three questions. After this first round is finished, it's the opponents turn to choose a new category and answer three questions out of this category. Now it's your turn to answer the same three questions. With this done, the 2nd round is finished. One game has seven rounds.
Please find attached the balsamiq project. For all of you, do not have balsamiq, please find also the mockups as pdf.
Final delivery should be psd files
Target Market(s)
Casual Games

```html
<!DOCTYPE html>
<html lang="en">
<head>
<meta charset="utf-8">
<title>Quizora – App Screens</title>
<link href="https://fonts.googleapis.com/css2?family=Roboto:wght@300;400;500&display=swap" rel="stylesheet">
<style>
:root{
  --stage:#1d0f2b;
  --stage-glow:#2c1840;
  --screen:#393b54;
  --screen-dark:#2f3046;
  --header:#34354c;
  --row-alt:#3f415b;
  --panel:#9c9bb5;
  --panel-dark:#8a89a3;
  --field:#424460;
  --text:#ffffff;
  --muted:#8d8fa8;
  --faint:#5c5e78;
  --green:#8be33a;
  --green-btn:#7fd441;
  --cyan:#14c6ef;
  --blue:#2d9fd9;
  --navy:#3c5a9c;
  --teal:#22bfae;
  --red:#f0495a;
  --pink:#e81d63;
  --orange:#f39a1e;
  --yellow:#e5e52e;
  --violet:#6c7cf2;
  --dot-off:#2b2c3e;
  --card:#dcdce2;
  --key:#3a3a3f;
  --keyboard:#26262b;
}
*{box-sizing:border-box;margin:0;padding:0}
html,body{width:1200px;height:800px;overflow:hidden}
body{background:radial-gradient(ellipse at 50% 45%,var(--stage-glow),var(--stage) 75%);font-family:'Roboto',sans-serif;color:var(--text);position:relative}
.screen{position:absolute;width:204px;height:360px;background:var(--screen);overflow:hidden}
.abs{position:absolute}

/* status bar */
.status{position:absolute;left:0;top:0;width:100%;height:14px;font-size:6px;display:flex;align-items:center;justify-content:space-between;padding:0 5px;background:var(--screen-dark);z-index:5}
.signal{display:flex;gap:1px;align-items:center}
.signal i{width:3px;height:3px;border-radius:50%;background:#fff;display:block}
.signal i.off{background:none;border:0.6px solid #fff}
.battery{display:flex;align-items:center;gap:2px}
.battery b{width:12px;height:5px;background:#fff;display:block;border-radius:1px}

/* header */
.header{position:absolute;left:0;top:14px;width:100%;height:30px;background:var(--header)}
.menu-icon{position:absolute;left:8px;top:10px;width:15px;height:10px;border-top:2px solid var(--faint);border-bottom:2px solid var(--faint)}
.menu-icon::after{content:"";position:absolute;left:0;top:2px;width:15px;height:2px;background:var(--faint)}
.app-title{position:absolute;left:0;width:100%;top:6px;text-align:center;font-size:15px;font-weight:300;color:var(--faint)}
.header.lit .menu-icon{border-color:#8a8ca6}
.header.lit .menu-icon::after{background:#8a8ca6}
.header.lit .app-title{color:#8a8ca6}

/* brand */
.brand-name{position:absolute;left:0;width:100%;top:98px;text-align:center;font-size:25px;font-weight:400;letter-spacing:0.3px}

/* forms */
.field{position:absolute;left:23px;width:156px;height:20px;background:var(--field);font-size:7px;color:var(--muted);display:flex;align-items:center;padding-left:8px;gap:8px}
.field i{width:5px;height:4px;background:var(--muted);display:block}
.btn{position:absolute;left:23px;width:156px;height:24px;font-size:9.5px;letter-spacing:1px;display:flex;align-items:center;justify-content:center}
.btn.green{background:var(--green)}
.btn.blue{background:var(--blue)}
.btn.cyan{background:var(--cyan)}
.btn.navy{background:var(--navy);letter-spacing:0.5px}
.note{position:absolute;left:0;width:100%;text-align:center;font-size:7px;color:var(--muted)}

/* keyboard */
.keyboard{position:absolute;left:0;top:250px;width:100%;height:110px;background:var(--keyboard);padding:6px 3px 0}
.krow{display:flex;justify-content:center;gap:3px;margin-bottom:6px}
.key{height:20px;width:17px;background:var(--key);border-radius:2px;font-size:9px;display:flex;align-items:center;justify-content:center}
.key.wide{width:25px;font-size:7px}
.key.space{width:78px;font-size:7px}
.key.ret{width:50px;font-size:7px}

/* avatars */
.avatar{position:absolute;border-radius:50%;border:2px solid #fff;background:radial-gradient(circle at 50% 40%,#c9a48e,#5a4438 75%)}
.avatar.dark{background:radial-gradient(circle at 50% 40%,#b89a8a,#2d2523 75%)}
.presence{position:absolute;width:7px;height:7px;border-radius:50%;border:1px solid #fff}

/* game list */
.profile{position:absolute;left:0;top:44px;width:100%;height:52px;background:#3e405a}
.profile .name{position:absolute;left:79px;top:14px;font-size:18px;font-weight:300}
.create{position:absolute;left:5px;top:96px;width:193px;height:36px;background:var(--teal);font-size:13px;font-weight:300;display:flex;align-items:center;padding-left:23px}
.create .arrow{position:absolute;right:0;top:0;width:38px;height:36px;border-left:1px solid rgba(255,255,255,.35);display:flex;align-items:center;justify-content:center}
.game{position:absolute;left:0;width:100%;height:54px;border-bottom:1px solid #33344a}
.game.alt{background:var(--row-alt)}
.game .state{position:absolute;right:16px;top:4px;font-size:7px}
.game .msg{position:absolute;left:84px;top:22px;font-size:8.5px}
.game .score{position:absolute;right:16px;top:19px;font-size:7px;text-align:right;line-height:9px}
.game .opp{position:absolute;right:16px;top:40px;font-size:7px;color:var(--faint)}
.scrollbar{position:absolute;right:1px;top:140px;width:2px;height:110px;background:#5a5c75}
.c-yellow{color:var(--yellow)}.c-violet{color:var(--violet)}.c-red{color:var(--red)}

/* side menu */
.drawer{position:absolute;left:0;top:14px;width:147px;height:346px;background:var(--screen-dark);z-index:4}
.drawer .menu-icon{border-color:#9a9cb4}
.drawer .menu-icon::after{background:#9a9cb4}
.drawer .app-title{left:0;width:204px;color:#9a9cb4}
.menu-item{position:absolute;left:0;width:147px;height:27px;border-bottom:1px solid #3a3b52;font-size:8.5px;color:#cfd0dc;display:flex;align-items:center}
.menu-item svg{position:absolute;left:14px}
.menu-item span{width:100%;text-align:center;padding-left:16px}
.signout{position:absolute;left:14px;top:330px;font-size:7.5px;color:#cfd0dc;display:flex;align-items:center;gap:46px}

/* scoreboard */
.board{position:absolute;left:0;top:44px;width:100%;height:316px;background:var(--panel)}
.board .player{position:absolute;font-size:7.5px;text-align:center;width:60px}
.board .tally{position:absolute;left:62px;width:80px;top:22px;text-align:center;font-size:19px;font-weight:300}
.round{position:absolute;left:0;width:100%;height:24.4px;background:var(--panel)}
.round.odd{background:var(--panel-dark)}
.dots{position:absolute;top:7px;display:flex;gap:6px}
.dots.left{left:23px}.dots.right{left:137px}
.dot{width:10px;height:10px;border-radius:50%;border:1.2px solid #fff;display:block}
.dot.g{background:var(--green)}.dot.r{background:var(--red)}.dot.k{background:var(--dot-off)}
.round .label{position:absolute;left:72px;width:58px;top:4px;text-align:center;font-size:7px;color:#e8e8f0;line-height:8px}
.round .label small{display:block;font-size:5.5px;color:#b7b6cb}
.action{position:absolute;left:20px;width:164px;height:29px;font-size:12px;font-weight:300;display:flex;align-items:center;justify-content:center}

/* search options */
.option{position:absolute;left:21px;width:163px;height:27px;border:1px solid #4a4c66;font-size:8.5px;color:#d6d7e2;display:flex;align-items:center}
.option svg{position:absolute;left:10px}
.option span{width:100%;text-align:center;padding-left:14px}

/* categories */
.category{position:absolute;left:0;width:100%;height:43px;background:var(--screen-dark);border-bottom:1px solid var(--screen)}
.category .swatch{position:absolute;left:0;top:0;width:44px;height:43px;display:flex;align-items:center;justify-content:center}
.category span{position:absolute;left:44px;right:0;top:14px;text-align:center;font-size:11.5px;font-weight:300;color:#d6d7e2}

/* question */
.question{position:absolute;left:4px;top:54px;width:196px;height:140px;background:var(--card);color:#2d2e40;font-size:12.5px;display:flex;align-items:center;justify-content:center}
.answer{position:absolute;width:93px;height:60px;background:#404159;font-size:7px;display:flex;align-items:center;justify-content:center}
.answer.right{background:var(--cyan)}
.answer.wrong{background:var(--pink)}
.answer svg{position:absolute;right:4px;bottom:4px}
</style>
</head>
<body>

<!-- ============ Sign in ============ -->
<section class="screen" style="left:68px;top:24px">
  <div class="status"><span class="signal"><i></i><i></i><i></i><i></i><i class="off"></i></span><span>11:14 PM</span><span class="battery">100% <b></b></span></div>
  <div class="brand-name">Quizora</div>
  <div class="field" style="top:138px"><i></i>Username</div>
  <div class="field" style="top:161px"><i></i>Password</div>
  <div class="btn green" style="top:183px">SIGN IN</div>
  <div class="btn blue" style="top:240px">SIGN UP</div>
  <div class="note" style="top:269px;font-style:italic;letter-spacing:1px">Create new account</div>
  <div class="abs" style="left:23px;top:285px;width:156px;height:1px;background:#55577a"></div>
  <div class="note" style="top:280px;left:88px;width:28px;background:var(--screen);font-size:8px">or</div>
  <div class="btn navy" style="top:294px">Login with Linkbook</div>
</section>

<!-- ============ Sign up ============ -->
<section class="screen" style="left:282px;top:24px">
  <div class="status"><span class="signal"><i></i><i></i><i></i><i></i><i class="off"></i></span><span>11:14 PM</span><span class="battery">100% <b></b></span></div>
  <div class="brand-name">Quizora</div>
  <div class="field" style="top:138px"><i></i>Username</div>
  <div class="field" style="top:161px"><i></i>Password</div>
  <div class="btn cyan" style="top:183px">SIGN UP</div>
  <div class="note" style="top:213px;color:#d6d7e2">Already have an account?</div>
  <div class="note" style="top:225px;color:var(--green);font-size:9.5px;letter-spacing:1px">SIGN IN</div>
  <div class="keyboard">
    <div class="krow"><span class="key">Q</span><span class="key">W</span><span class="key">E</span><span class="key">R</span><span class="key">T</span><span class="key">Y</span><span class="key">U</span><span class="key">I</span><span class="key">O</span><span class="key">P</span></div>
    <div class="krow"><span class="key">A</span><span class="key">S</span><span class="key">D</span><span class="key">F</span><span class="key">G</span><span class="key">H</span><span class="key">J</span><span class="key">K</span><span class="key">L</span></div>
    <div class="krow"><span class="key wide"><svg width="9" height="9" viewBox="0 0 10 10"><path d="M5 1 L9 5 H7 V9 H3 V5 H1 Z" fill="#fff"/></svg></span><span class="key">Z</span><span class="key">X</span><span class="key">C</span><span class="key">V</span><span class="key">B</span><span class="key">N</span><span class="key">M</span><span class="key wide"><svg width="11" height="8" viewBox="0 0 12 8"><path d="M3 0 H12 V8 H3 L0 4 Z" fill="#fff"/></svg></span></div>
    <div class="krow"><span class="key wide">123</span><span class="key wide"><svg width="9" height="9" viewBox="0 0 10 10"><circle cx="5" cy="5" r="4" fill="none" stroke="#fff"/><path d="M1 5 H9 M5 1 V9" stroke="#fff" stroke-width=".8"/></svg></span><span class="key wide"><svg width="6" height="9" viewBox="0 0 6 10"><rect x="1.5" y="0" width="3" height="6" rx="1.5" fill="#fff"/><path d="M0.5 5 Q3 9 5.5 5 M3 8 V10" stroke="#fff" fill="none" stroke-width=".8"/></svg></span><span class="key space">space</span><span class="key ret">return</span></div>
  </div>
</section>

<!-- ============ Games list ============ -->
<section class="screen" style="left:497px;top:24px">
  <div class="status"><span class="signal"><i></i><i></i><i></i><i></i><i class="off"></i></span><span>11:14 PM</span><span class="battery">100% <b></b></span></div>
  <div class="header"><div class="menu-icon"></div><div class="app-title">Quizora</div></div>
  <div class="profile">
    <div class="avatar dark" role="img" aria-label="Profile photo of the player" style="left:10px;top:5px;width:42px;height:42px"></div>
    <div class="name">Username</div>
  </div>
  <div class="create">Create New Game<div class="arrow"><svg width="10" height="16" viewBox="0 0 10 16"><path d="M1 1 L9 8 L1 15" stroke="#fff" stroke-width="1.6" fill="none"/></svg></div></div>
  <div class="game" style="top:145px">
    <div class="avatar" role="img" aria-label="Opponent photo" style="left:9px;top:6px;width:42px;height:42px"></div><span class="presence" style="left:44px;top:7px;background:var(--green)"></span>
    <div class="state c-yellow">Game is Underway</div><div class="msg">your turn</div>
    <div class="score">3 : 1<br>Round 3</div><div class="opp">player username</div>
  </div>
  <div class="game alt" style="top:199px">
    <div class="avatar" role="img" aria-label="Opponent photo" style="left:9px;top:6px;width:42px;height:42px"></div><span class="presence" style="left:44px;top:7px;background:var(--red)"></span>
    <div class="state c-yellow">Game is Underway</div><div class="msg">waiting for player</div>
    <div class="score">3 : 5<br>Round 6</div><div class="opp">player username</div>
  </div>
  <div class="game" style="top:253px">
    <div class="avatar dark" role="img" aria-label="Opponent photo" style="left:9px;top:6px;width:42px;height:42px"></div><span class="presence" style="left:44px;top:7px;background:var(--violet)"></span>
    <div class="state c-violet">Finished Game</div><div class="msg c-yellow">You are Winner</div>
    <div class="score">6 : 4<br>Round 7</div><div class="opp">player username</div>
  </div>
  <div class="game alt" style="top:307px">
    <div class="avatar" role="img" aria-label="Opponent photo" style="left:9px;top:6px;width:42px;height:42px"></div><span class="presence" style="left:44px;top:7px;background:var(--violet)"></span>
    <div class="state c-violet">Finished Game</div><div class="msg c-red">You are Lose</div>
    <div class="score">3 : 7<br>Round 7</div><div class="opp">player username</div>
  </div>
  <div class="scrollbar"></div>
</section>

<!-- ============ Side menu ============ -->
<section class="screen" style="left:711px;top:24px">
  <div class="status"><span class="signal"><i></i><i></i><i></i><i></i><i class="off"></i></span><span>11:14 PM</span><span class="battery">100% <b></b></span></div>
  <div class="header"></div>
  <div class="profile"><div class="name">Username</div></div>
  <div class="create">Create New Game<div class="arrow"><svg width="10" height="16" viewBox="0 0 10 16"><path d="M1 1 L9 8 L1 15" stroke="#fff" stroke-width="1.6" fill="none"/></svg></div></div>
  <div class="game" style="top:145px"><div class="state c-yellow">Game is Underway</div><div class="score">3 : 1<br>Round 3</div><div class="opp">player username</div></div>
  <div class="game alt" style="top:199px"><div class="state c-yellow">Game is Underway</div><div class="score">3 : 5<br>Round 6</div><div class="opp">player username</div></div>
  <div class="game" style="top:253px"><div class="state c-violet">Finished Game</div><div class="score">6 : 4<br>Round 7</div><div class="opp">player username</div></div>
  <div class="game alt" style="top:307px"><div class="state c-violet">Finished Game</div><div class="score">3 : 7<br>Round 7</div><div class="opp">player username</div></div>
  <div class="scrollbar"></div>
  <nav class="drawer">
    <div class="menu-icon"></div><div class="app-title">Quizora</div>
    <div class="menu-item" style="top:30px"><svg width="10" height="10" viewBox="0 0 10 10"><circle cx="5" cy="3" r="2.5" fill="#cfd0dc"/><path d="M0.5 10 Q5 4 9.5 10Z" fill="#cfd0dc"/></svg><span>Overview</span></div>
    <div class="menu-item" style="top:57px"><svg width="13" height="10" viewBox="0 0 13 10"><circle cx="6.5" cy="3" r="2.3" fill="#cfd0dc"/><circle cx="2.3" cy="4" r="1.6" fill="#cfd0dc"/><circle cx="10.7" cy="4" r="1.6" fill="#cfd0dc"/><path d="M2.5 10 Q6.5 4 10.5 10Z M0 9 Q2 5.5 4 8Z M13 9 Q11 5.5 9 8Z" fill="#cfd0dc"/></svg><span>My Groups</span></div>
    <div class="menu-item" style="top:84px"><svg width="12" height="10" viewBox="0 0 12 10"><circle cx="4" cy="3" r="2.3" fill="#cfd0dc"/><path d="M0 10 Q4 4 8 10Z M9.5 2 V6 M7.5 4 H11.5" fill="#cfd0dc" stroke="#cfd0dc"/></svg><span>Invite Friend</span></div>
    <div class="menu-item" style="top:111px"><svg width="11" height="9" viewBox="0 0 11 9"><rect x="0" y="4" width="2" height="5" fill="#cfd0dc"/><rect x="3" y="1" width="2" height="8" fill="#cfd0dc"/><rect x="6" y="3" width="2" height="6" fill="#cfd0dc"/><rect x="9" y="0" width="2" height="9" fill="#cfd0dc"/></svg><span>Statistic</span></div>
    <div class="menu-item" style="top:138px"><svg width="10" height="10" viewBox="0 0 10 10"><circle cx="5" cy="5" r="3.5" fill="none" stroke="#cfd0dc" stroke-width="2.4" stroke-dasharray="1.8 1"/><circle cx="5" cy="5" r="1.4" fill="#cfd0dc"/></svg><span>Help</span></div>
    <div class="menu-item" style="top:165px"><svg width="11" height="10" viewBox="0 0 11 10"><rect x="2.5" y="0" width="6" height="3" fill="none" stroke="#cfd0dc"/><rect x="0.5" y="3" width="10" height="5" fill="none" stroke="#cfd0dc"/><rect x="2.5" y="6" width="6" height="4" fill="#cfd0dc"/></svg><span>Imprint</span></div>
    <div class="signout"><svg width="10" height="10" viewBox="0 0 10 10"><path d="M0 1 H6 V3 M6 7 V9 H0 Z" fill="none" stroke="#cfd0dc"/><path d="M4 5 H10 M8 3 L10 5 L8 7" stroke="#cfd0dc" fill="none"/></svg><span>SIGN OUT</span></div>
  </nav>
</section>

<!-- ============ Resume game ============ -->
<section class="screen" style="left:926px;top:24px">
  <div class="status"><span class="signal"><i></i><i></i><i></i><i></i><i class="off"></i></span><span>11:14 PM</span><span class="battery">100% <b></b></span></div>
  <div class="header lit"><div class="menu-icon"></div><div class="app-title">Quizora</div></div>
  <div class="board">
    <div class="avatar" role="img" aria-label="Player photo" style="left:24px;top:12px;width:42px;height:42px"></div>
    <div class="avatar" role="img" aria-label="Opponent photo" style="left:137px;top:12px;width:42px;height:42px"></div>
    <div class="player" style="left:15px;top:57px">Username</div>
    <div class="player" style="left:128px;top:57px">Username</div>
    <div class="tally">6 :4</div>
    <div class="round odd" style="top:72px"><div class="dots left"><i class="dot g"></i><i class="dot r"></i><i class="dot g"></i></div><div class="label">Round 1<small>Category</small></div><div class="dots right"><i class="dot g"></i><i class="dot r"></i><i class="dot g"></i></div></div>
    <div class="round" style="top:96.4px"><div class="dots left"><i class="dot g"></i><i class="dot r"></i><i class="dot g"></i></div><div class="label">Round 2<small>Category</small></div><div class="dots right"><i class="dot g"></i><i class="dot r"></i><i class="dot g"></i></div></div>
    <div class="round odd" style="top:120.8px"><div class="dots left"><i class="dot g"></i><i class="dot g"></i><i class="dot r"></i></div><div class="label">Round 3<small>Category</small></div><div class="dots right"><i class="dot k"></i><i class="dot k"></i><i class="dot k"></i></div></div>
    <div class="round" style="top:145.2px"><div class="dots left"><i class="dot k"></i><i class="dot k"></i><i class="dot k"></i></div><div class="label">Round 4<small>Category</small></div><div class="dots right"><i class="dot k"></i><i class="dot k"></i><i class="dot k"></i></div></div>
    <div class="round odd" style="top:169.6px"><div class="dots left"><i class="dot k"></i><i class="dot k"></i><i class="dot k"></i></div><div class="label">Round 5<small>Category</small></div><div class="dots right"><i class="dot k"></i><i class="dot k"></i><i class="dot k"></i></div></div>
    <div class="round" style="top:194px"><div class="dots left"><i class="dot k"></i><i class="dot k"></i><i class="dot k"></i></div><div class="label">Round 6<small>Category</small></div><div class="dots right"><i class="dot k"></i><i class="dot k"></i><i class="dot k"></i></div></div>
    <div class="round odd" style="top:218.4px"><div class="dots left"><i class="dot k"></i><i class="dot k"></i><i class="dot k"></i></div><div class="label">Round 7<small>Category</small></div><div class="dots right"><i class="dot k"></i><i class="dot k"></i><i class="dot k"></i></div></div>
    <div class="action" style="top:255px;background:var(--green-btn)">Resume Game</div>
  </div>
</section>

<!-- ============ Waiting ============ -->
<section class="screen" style="left:68px;top:412px">
  <div class="status"><span class="signal"><i></i><i></i><i></i><i></i><i class="off"></i></span><span>11:14 PM</span><span class="battery">100% <b></b></span></div>
  <div class="header lit"><div class="menu-icon"></div><div class="app-title">Quizora</div></div>
  <div class="board">
    <div class="avatar" role="img" aria-label="Player photo" style="left:24px;top:12px;width:42px;height:42px"></div>
    <div class="avatar" role="img" aria-label="Opponent photo" style="left:137px;top:12px;width:42px;height:42px"></div>
    <div class="player" style="left:15px;top:57px">Username</div>
    <div class="player" style="left:128px;top:57px">Username</div>
    <div class="tally">6 :4</div>
    <div class="round odd" style="top:72px"><div class="dots left"><i class="dot g"></i><i class="dot r"></i><i class="dot g"></i></div><div class="label">Round 1<small>Category</small></div><div class="dots right"><i class="dot g"></i><i class="dot r"></i><i class="dot g"></i></div></div>
    <div class="round" style="top:96.4px"><div class="dots left"><i class="dot g"></i><i class="dot r"></i><i class="dot g"></i></div><div class="label">Round 2<small>Category</small></div><div class="dots right"><i class="dot g"></i><i class="dot r"></i><i class="dot g"></i></div></div>
    <div class="round odd" style="top:120.8px"><div class="dots left"><i class="dot g"></i><i class="dot g"></i><i class="dot r"></i></div><div class="label">Round 3<small>Category</small></div><div class="dots right"><i class="dot k"></i><i class="dot k"></i><i class="dot k"></i></div></div>
    <div class="round" style="top:145.2px"><div class="dots left"><i class="dot k"></i><i class="dot k"></i><i class="dot k"></i></div><div class="label">Round 4<small>Category</small></div><div class="dots right"><i class="dot k"></i><i class="dot k"></i><i class="dot k"></i></div></div>
    <div class="round odd" style="top:169.6px"><div class="dots left"><i class="dot k"></i><i class="dot k"></i><i class="dot k"></i></div><div class="label">Round 5<small>Category</small></div><div class="dots right"><i class="dot k"></i><i class="dot k"></i><i class="dot k"></i></div></div>
    <div class="round" style="top:194px"><div class="dots left"><i class="dot k"></i><i class="dot k"></i><i class="dot k"></i></div><div class="label">Round 6<small>Category</small></div><div class="dots right"><i class="dot k"></i><i class="dot k"></i><i class="dot k"></i></div></div>
    <div class="round odd" style="top:218.4px"><div class="dots left"><i class="dot k"></i><i class="dot k"></i><i class="dot k"></i></div><div class="label">Round 7<small>Category</small></div><div class="dots right"><i class="dot k"></i><i class="dot k"></i><i class="dot k"></i></div></div>
    <div class="action" style="top:255px;background:var(--red)">Waiting</div>
  </div>
</section>

<!-- ============ Final score ============ -->
<section class="screen" style="left:282px;top:412px">
  <div class="status"><span class="signal"><i></i><i></i><i></i><i></i><i class="off"></i></span><span>11:14 PM</span><span class="battery">100% <b></b></span></div>
  <div class="header lit"><div class="menu-icon"></div><div class="app-title">Quizora</div></div>
  <div class="board">
    <div class="avatar" role="img" aria-label="Player photo" style="left:24px;top:12px;width:42px;height:42px"></div>
    <div class="avatar" role="img" aria-label="Opponent photo" style="left:137px;top:12px;width:42px;height:42px"></div>
    <div class="player" style="left:15px;top:57px">Username</div>
    <div class="player" style="left:128px;top:57px">Username</div>
    <div class="tally">12 :10</div>
    <div class="round odd" style="top:72px"><div class="dots left"><i class="dot g"></i><i class="dot r"></i><i class="dot g"></i></div><div class="label">Round 1<small>Category</small></div><div class="dots right"><i class="dot g"></i><i class="dot r"></i><i class="dot g"></i></div></div>
    <div class="round" style="top:96.4px"><div class="dots left"><i class="dot g"></i><i class="dot r"></i><i class="dot g"></i></div><div class="label">Round 2<small>Category</small></div><div class="dots right"><i class="dot g"></i><i class="dot r"></i><i class="dot g"></i></div></div>
    <div class="round odd" style="top:120.8px"><div class="dots left"><i class="dot g"></i><i class="dot g"></i><i class="dot r"></i></div><div class="label">Round 3<small>Category</small></div><div class="dots right"><i class="dot g"></i><i class="dot r"></i><i class="dot r"></i></div></div>
    <div class="round" style="top:145.2px"><div class="dots left"><i class="dot g"></i><i class="dot g"></i><i class="dot r"></i></div><div class="label">Round 4<small>Category</small></div><div class="dots right"><i class="dot g"></i><i class="dot r"></i><i class="dot g"></i></div></div>
    <div class="round odd" style="top:169.6px"><div class="dots left"><i class="dot r"></i><i class="dot r"></i><i class="dot g"></i></div><div class="label">Round 5<small>Category</small></div><div class="dots right"><i class="dot g"></i><i class="dot g"></i><i class="dot g"></i></div></div>
    <div class="round" style="top:194px"><div class="dots left"><i class="dot r"></i><i class="dot g"></i><i class="dot g"></i></div><div class="label">Round 6<small>Category</small></div><div class="dots right"><i class="dot r"></i><i class="dot r"></i><i class="dot r"></i></div></div>
    <div class="round odd" style="top:218.4px"><div class="dots left"><i class="dot r"></i><i class="dot g"></i><i class="dot g"></i></div><div class="label">Round 7<small>Category</small></div><div class="dots right"><i class="dot r"></i><i class="dot r"></i><i class="dot g"></i></div></div>
  </div>
</section>

<!-- ============ Find opponent ============ -->
<section class="screen" style="left:499px;top:412px">
  <div class="status"><span class="signal"><i></i><i></i><i></i><i></i><i class="off"></i></span><span>11:14 PM</span><span class="battery">100% <b></b></span></div>
  <div class="header"><div class="menu-icon"></div><div class="app-title">Quizora</div></div>
  <div class="option" style="top:93px"><svg width="14" height="11" viewBox="0 0 14 11"><circle cx="5" cy="3" r="2.5" fill="#d6d7e2"/><circle cx="10" cy="4" r="2" fill="#d6d7e2"/><path d="M0 11 Q5 4 10 11Z M8 11 Q10 6 14 10Z" fill="#d6d7e2"/></svg><span>Search for Players</span></div>
  <div class="option" style="top:138px"><svg width="13" height="13" viewBox="0 0 13 13"><circle cx="6.5" cy="6.5" r="6.5" fill="#d6d7e2"/></svg><span>Linkbook Friend</span></div>
  <div class="option" style="top:184px"><svg width="13" height="13" viewBox="0 0 13 13"><circle cx="6.5" cy="6.5" r="5.8" fill="none" stroke="#d6d7e2" stroke-width="1.2"/><path d="M0.7 6.5 H12.3 M6.5 0.7 Q2.5 6.5 6.5 12.3 M6.5 0.7 Q10.5 6.5 6.5 12.3" stroke="#d6d7e2" fill="none" stroke-width=".9"/></svg><span>Random Players</span></div>
</section>

<!-- ============ Choose category ============ -->
<section class="screen" style="left:717px;top:412px">
  <div class="status"><span class="signal"><i></i><i></i><i></i><i></i><i class="off"></i></span><span>11:14 PM</span><span class="battery">100% <b></b></span></div>
  <div class="header"><div class="menu-icon"></div><div class="app-title">Quizora</div></div>
  <div class="category" style="top:116px"><div class="swatch" style="background:var(--blue)"><svg width="16" height="16" viewBox="0 0 16 16"><circle cx="8" cy="8" r="7" fill="none" stroke="#1d2a44" stroke-width="1.6"/><path d="M1 8 H15 M8 1 V15 M3 3 Q8 8 3 13 M13 3 Q8 8 13 13" stroke="#1d2a44" fill="none" stroke-width="1.3"/></svg></div><span>Category</span></div>
  <div class="category" style="top:160px"><div class="swatch" style="background:var(--green)"><svg width="17" height="14" viewBox="0 0 17 14"><rect x="0.8" y="2.8" width="15.4" height="10.4" rx="1" fill="none" stroke="#1d2a24" stroke-width="1.6"/><rect x="5" y="0.5" width="7" height="3" fill="#1d2a24"/><circle cx="8.5" cy="8" r="3" fill="none" stroke="#1d2a24" stroke-width="1.6"/></svg></div><span>Category</span></div>
  <div class="category" style="top:204px"><div class="swatch" style="background:var(--orange)"><svg width="16" height="16" viewBox="0 0 16 16"><circle cx="8" cy="8" r="7" fill="#1d2a44"/><path d="M4 3 Q7 5 5 8 Q8 10 6 14 M10 2 Q9 6 12 7 Q14 9 13 12" stroke="#f39a1e" fill="none" stroke-width="1.4"/></svg></div><span>Category</span></div>
  <div class="category" style="top:248px"><div class="swatch" style="background:var(--red)"><svg width="16" height="14" viewBox="0 0 16 14"><path d="M8 14 L1.5 7.5 A3.8 3.8 0 0 1 8 2.5 A3.8 3.8 0 0 1 14.5 7.5 Z" fill="#3a1a24"/></svg></div><span>Category</span></div>
</section>

<!-- ============ Question ============ -->
<section class="screen" style="left:933px;top:412px">
  <div class="status"><span class="signal"><i></i><i></i><i></i><i></i><i class="off"></i></span><span>11:14 PM</span><span class="battery">100% <b></b></span></div>
  <div class="header"><div class="menu-icon"></div><div class="app-title">Quizora</div></div>
  <div class="question">Question?</div>
  <div class="answer" style="left:6px;top:201px">Answer</div>
  <div class="answer right" style="left:105px;top:201px">Answer<svg width="12" height="12" viewBox="0 0 12 12"><circle cx="6" cy="6" r="5.3" fill="none" stroke="#fff"/><path d="M3.3 6.2 L5.2 8 L8.8 4.2" stroke="#fff" fill="none"/></svg></div>
  <div class="answer" style="left:6px;top:266px">Answer</div>
  <div class="answer wrong" style="left:105px;top:266px">Answer<svg width="12" height="12" viewBox="0 0 12 12"><circle cx="6" cy="6" r="5.3" fill="none" stroke="#fff"/><path d="M4 4 L8 8 M8 4 L4 8" stroke="#fff"/></svg></div>
</section>

</body>
</html>
```